Redesign MuseQuill's Artist Profile Page

MuseQuill is a contemporary arts website that has a large worldwide community of artists with profile pages for each artist showing artwork, exhibits, bio data, etc.

For an example please see: http://www.musequill-example.com/global/artists/show/47302-dorian-pell

We would like a slight redesign on these pages within the context of the current website. We are interested in modernizing and lightening the design. The artwork should be the primary focus.

Target Market(s)

Professional artists, galleries and collectors

Industry/Entity Type

Artists

Requirements
Must have
• All the current functionality on the page.

```html
<!DOCTYPE html>
<html lang="en">
<head>
<meta charset="utf-8">
<title>MuseQuill – Artist Profile</title>
<link rel="stylesheet" href="https://fonts.googleapis.com/css2?family=Jost:ital,wght@0,300;0,400;0,500;0,600;1,300;1,400;1,500&family=Barlow+Condensed:ital,wght@0,600;0,700;1,500&display=swap">
<style>
:root{
  --bg:#1f1f1f;
  --ink:#ffffff;
  --ink-soft:#d8d8d8;
  --ink-muted:#9a9a9a;
  --bar:#000000;
  --pink:#e0287a;
  --menu-top:#3c3c3c;
  --menu-bottom:#565656;
  --menu-text:#c4c4c4;
  --panel:#4a4a4a;
  --panel-head-top:#d6d6d6;
  --panel-head-bottom:#9c9c9c;
  --accent-red:#c8202a;
}
*{margin:0;padding:0;box-sizing:border-box}
html,body{width:1200px;height:900px;overflow:hidden}
body{background:var(--bg);color:var(--ink);font-family:"Jost",sans-serif;position:relative}
.abs{position:absolute}

/* top */
.city-picker{left:465px;top:4px;width:266px;height:22px;display:flex;border-radius:4px;overflow:hidden;background:linear-gradient(#f0f0f0,#bdbdbd);font-family:"Barlow Condensed",sans-serif;font-weight:700;font-size:13px;letter-spacing:.3px}
.city-picker .label{width:138px;color:#333;padding:3px 0 0 5px;border-right:1px solid #999}
.city-picker .value{flex:1;color:var(--pink);padding:3px 0 0 16px;font-family:"Jost",sans-serif;font-weight:400;font-size:12px}
.city-picker .value::after{content:"▾";color:#666;margin-left:6px}
.utility-links{right:103px;top:27px;font-size:12px;color:var(--ink-soft)}
.utility-links span{margin:0 7px;color:#aaa}

.brand{left:140px;top:66px;display:flex;align-items:center;gap:10px}
.brand .mark{width:30px;height:30px;background:var(--ink)}
.brand .name{font-size:34px;font-weight:500;color:var(--ink);line-height:1}

.main-nav{left:457px;top:64px;width:653px;height:38px;background:var(--bar);display:flex;align-items:center;padding-left:36px;gap:24px;font-size:17px;font-weight:300;color:var(--ink-soft)}

/* left column */
.artist-title{left:116px;top:153px;font-size:27px;font-weight:300;line-height:31px;letter-spacing:.5px}
.artist-title em{font-style:italic;font-weight:300}
.artist-title .slashes{display:inline-block;vertical-align:-3px;margin-left:8px}
.preview-tab{left:90px;top:283px;width:260px;height:37px;background:#fff;color:#3a3a3a;font-family:"Barlow Condensed",sans-serif;font-weight:600;font-size:17px;letter-spacing:.9px;text-align:right;padding:8px 10px 0 0}
.preview-tab::after{content:"  ▸";color:#888;white-space:pre}
.profile-menu{left:101px;top:329px;width:249px;list-style:none;background:var(--menu-bottom);padding-bottom:10px}
.profile-menu li{height:36px;background:linear-gradient(var(--menu-top),var(--menu-bottom));border-top:1px solid #666;border-bottom:1px solid #2a2a2a;font-family:"Barlow Condensed",sans-serif;font-weight:700;font-size:16px;color:var(--menu-text);padding:8px 0 0 35px;letter-spacing:.3px}

/* gallery */
.feature-frame{left:350px;top:147px;width:500px;height:407px;background:#fff;padding:6px 7px 6px 8px}
.feature-art{width:100%;height:100%;background:linear-gradient(135deg,#5a1418 0%,#2a2020 40%,#1a2a3a 70%,#e8e0d8 100%)}
.thumbs{left:362px;top:564px;display:flex;gap:6px}
.thumbs div{width:73px;height:73px;border:2px solid #ddd}
.t1{background:linear-gradient(135deg,#c8a020,#3a2a40)}
.t2{background:linear-gradient(135deg,#3a2018,#c09070)}
.t3{background:linear-gradient(135deg,#f0f0f0,#6a1a1a)}
.t4{background:linear-gradient(135deg,#4aa0d0,#e0c0a0)}
.t5{background:linear-gradient(135deg,#1a3050,#d0d8e0)}
.t6{background:linear-gradient(135deg,#2a2a3a,#8a5a5a)}
.arrow{top:592px;width:24px;height:24px}

/* right column */
.search{left:884px;top:148px;display:flex;gap:5px}
.search .field{width:150px;height:22px;background:#fff;border:1px solid #7aa0d0;font-size:11px;font-style:italic;color:#999;padding:3px 5px}
.search .go{width:57px;height:18px;margin-top:2px;background:#000;color:#fff;font-size:12px;text-align:center;padding-top:1px}
.side-heading{font-size:18px;font-weight:500;letter-spacing:.4px;text-align:center;width:190px}
.news{left:890px;top:227px;width:224px;font-weight:500;font-style:italic;font-size:14px;color:var(--ink-muted);line-height:17px;letter-spacing:.2px}
.news p{margin-bottom:16px}
.news a{color:#b0b0b0;text-decoration:underline}
.actions{left:890px;top:431px;list-style:none;font-size:14px;color:var(--ink-soft)}
.actions li{height:24px;display:flex;align-items:center}
.actions svg{width:36px;height:20px;margin-right:5px}
.social{left:937px;top:614px}
.social .share{display:flex;gap:4px;align-items:center}
.pill{background:#dbe9f3;border:1px solid #9bb8cc;border-radius:3px;font-size:10px;color:#335;padding:1px 6px;height:17px}
.count{background:#fff;border:1px solid #ccc;font-size:10px;color:#333;padding:1px 5px;height:17px}
.like{margin-top:6px;width:48px;height:20px;background:#e8ecf4;border:1px solid #aab;border-radius:2px;font-size:10px;color:#334;padding:2px 0 0 16px}

/* info panels */
.panel{top:690px}
.panel-head{height:32px;background:linear-gradient(var(--panel-head-top),var(--panel-head-bottom));color:#111;font-size:18px;padding:2px 0 0 25px;box-shadow:0 3px 4px rgba(0,0,0,.5)}
.panel-body{background:var(--panel);margin-left:12px;font-size:15px;color:var(--ink)}
.quick-facts{left:178px;width:304px}
.quick-facts .panel-body{height:75px;display:grid;grid-template-columns:144px 1fr;align-content:start;padding:10px 0 0 13px;row-gap:7px;line-height:22px}
.quick-facts em{color:#ddd}
.statement{left:500px;width:510px}
.statement .panel-body{height:75px;padding:9px 14px 0 16px;line-height:18px;font-size:16px;letter-spacing:.3px}
.statement .more{font-style:italic;color:#9a9a9a;margin-left:6px}

/* footer */
.footer-nav{left:120px;top:836px;width:960px;height:28px;background:var(--bar);font-family:"Barlow Condensed",sans-serif;font-style:italic;font-weight:500;font-size:18px;color:#fff}
.footer-nav span{position:absolute;top:3px}
.copyright{left:0;top:871px;width:1200px;text-align:center;font-family:"Barlow Condensed",sans-serif;font-style:italic;font-weight:500;font-size:16px;color:#eee}
</style>
</head>
<body>

<div class="abs city-picker"><div class="label">CHOOSE YOUR CITY</div><div class="value">SAN FRANCISCO</div></div>
<div class="abs utility-links">Register Free<span>|</span>Sign In<span>|</span>FAQ</div>

<div class="abs brand"><div class="mark"></div><div class="name">MuseQuill</div></div>

<nav class="abs main-nav"><span>Home</span><span>Magazine</span><span>Calendar</span><span>Galleries</span><span>Art</span><span>Shop</span><span>Artists</span><span>Community</span></nav>

<h1 class="abs artist-title">MARCUS<br>LEITH<br>HOLLOWAY'S<br><em>Photography</em><svg class="slashes" width="40" height="24" viewBox="0 0 40 24"><path d="M8 0h6L6 24H0zM21 0h6l-8 24h-6z" fill="var(--accent-red)"/><path d="M34 0h6l-8 24h-6z" fill="#fff"/></svg></h1>

<div class="abs preview-tab">PREVIEW CONTENT</div>
<ul class="abs profile-menu">
  <li>PROFILE</li><li>ARTWORKS</li><li>FOR SALE</li><li>NETWORK</li><li>REVIEWS</li><li>COMMENTS</li>
</ul>

<div class="abs feature-frame"><div class="feature-art" role="img" aria-label="Featured photograph: a staged party scene in a red salon with guests around a table"></div></div>

<svg class="abs arrow" style="left:318px" viewBox="0 0 24 24"><circle cx="12" cy="12" r="12" fill="#000"/><path d="M14 6l-6 6 6 6" stroke="#fff" stroke-width="3" fill="none"/></svg>
<div class="abs thumbs">
  <div class="t1" role="img" aria-label="Thumbnail: fashion couple on yellow backdrop"></div>
  <div class="t2" role="img" aria-label="Thumbnail: portrait with gold headpiece"></div>
  <div class="t3" role="img" aria-label="Thumbnail: salon party scene"></div>
  <div class="t4" role="img" aria-label="Thumbnail: seated model by blue shutters"></div>
  <div class="t5" role="img" aria-label="Thumbnail: figure on coastal rocks"></div>
  <div class="t6" role="img" aria-label="Thumbnail: model with scarf in a car"></div>
</div>
<svg class="abs arrow" style="left:855px" viewBox="0 0 24 24"><circle cx="12" cy="12" r="12" fill="#000"/><path d="M10 6l6 6-6 6" stroke="#fff" stroke-width="3" fill="none"/></svg>

<div class="abs search"><div class="field">Type Here to Search</div><div class="go">Search</div></div>

<h2 class="abs side-heading" style="left:889px;top:197px">NEWS &amp; BUZZ</h2>
<div class="abs news">
  <p>Watch this artists - Round<br>&nbsp;&nbsp;#2 Entries</p>
  <p><a>Owen Marsh - 2012 Halvorsen<br>Award Winner</a></p>
  <p>Sekou Diarra: On our Worldwide<br>Watchlist</p>
</div>

<h2 class="abs side-heading" style="left:884px;top:383px">ACTIONS</h2>
<ul class="abs actions">
  <li><svg viewBox="0 0 36 20"><rect x="0" y="5" width="32" height="11" rx="2" fill="#666"/><text x="3" y="13.5" font-size="7" fill="#fff" font-family="Jost,sans-serif">ADD +</text></svg>add to my list</li>
  <li><svg viewBox="0 0 36 20"><rect x="7" y="4" width="22" height="12" rx="1" fill="#777"/><rect x="7" y="7" width="22" height="2" fill="#333"/></svg>view larger slideshow</li>
  <li><svg viewBox="0 0 36 20"><rect x="7" y="4" width="22" height="13" fill="#777"/><path d="M7 4l11 7 11-7" stroke="#333" stroke-width="1.5" fill="none"/></svg>email this artist</li>
  <li><svg viewBox="0 0 36 20"><path d="M10 2h16v8c0 5-8 9-8 9s-8-4-8-9z" fill="#777"/><path d="M13 9l4 4 6-6" stroke="#222" stroke-width="2" fill="none"/></svg>report abuse</li>
  <li><svg viewBox="0 0 36 20"><circle cx="18" cy="6" r="5" fill="#777"/><path d="M8 20c0-6 4-8 10-8s10 2 10 8z" fill="#777"/></svg>contact us for help</li>
  <li><svg viewBox="0 0 36 20"><rect x="9" y="0" width="20" height="20" rx="2" fill="#ccc"/></svg>pin this</li>
  <li><svg viewBox="0 0 36 20"><rect x="9" y="0" width="20" height="20" rx="2" fill="#3a9a4a"/></svg>drift it</li>
</ul>
<div class="abs social">
  <div class="share"><div class="pill">Share</div><div class="count">7,231</div></div>
  <div class="like">Like</div>
</div>

<section class="abs panel quick-facts">
  <div class="panel-head">Quick Facts</div>
  <div class="panel-body">
    <div>Birthplace: <em>Paris</em></div><div>Lives in: <em>Paris</em></div>
    <div>Birth year: <em>1974</em></div><div>Works in: <em>Paris</em></div>
  </div>
</section>
<section class="abs panel statement">
  <div class="panel-head">Statement</div>
  <div class="panel-body">Marcus Holloway lives and works in and around Paris. His photography has been shown in all kinds of small galleries, clubs, and alternative arts spaces. <span class="more">more</span></div>
</section>

<footer>
  <div class="abs footer-nav">
    <span style="left:136px">Contact</span><span style="left:243px">About</span><span style="left:351px">Advertise</span><span style="left:496px">Terms</span><span style="left:602px">Join the Team</span><span style="left:783px">FAQ</span>
  </div>
  <div class="abs copyright">Copyright © 2012-2099 by MuseQuill, Inc. All images and content remain the © of their rightful owners.</div>
</footer>

</body>
</html>
```